Accountant services flyer & marketing portfolio

I require a design for a marketing portfolio of blank templates for a flyer, product brochure, report cover for A4 based on our style - current logo, letterhead, website look and feel - that can be updated in publisher or word with relevant marketing and company information editorial material and text. It will be either printed A4 or saved as PDF and distributed

Target Market(s)

small business and investment / superfund clients

Industry/Entity Type

Accountant

Font styles to use
Sans Serif

Requirements
Must have
• Instyle of letterhead and website
Professional body logos
Space to input text
Relevant happy images
Nice to have
• Images of happy lifestyle types retirees, young families and mid-aged
tradesmen and professionals

```html
<!DOCTYPE html>
<html lang="en">
<head>
<meta charset="utf-8">
<title>Meridian Advisory – Flyer</title>
<link href="https://fonts.googleapis.com/css2?family=Arimo:wght@400;700&display=swap" rel="stylesheet">
<style>
  :root {
    --bg: #cfcfcf;
    --paper: #ffffff;
    --orange: #e8552b;
    --orange-deep: #d9441f;
    --orange-light: #f08a2c;
    --ink: #1e1e1e;
    --white: #ffffff;
  }
  * { margin: 0; padding: 0; box-sizing: border-box; }
  html, body {
    width: 1200px; height: 960px; overflow: hidden;
    background: var(--bg);
    font-family: "Arimo", Arial, sans-serif;
  }
  .flyer {
    position: absolute; left: 280px; top: 27px;
    width: 640px; height: 906px;
    background: var(--paper);
    overflow: hidden;
    box-shadow: 0 6px 20px rgba(0,0,0,0.25);
  }
  .hero-photo {
    position: absolute; inset: 0;
    background:
      radial-gradient(ellipse at 70% 35%, #c99a7c 0%, rgba(201,154,124,0) 40%),
      radial-gradient(ellipse at 40% 62%, #e9c9a4 0%, rgba(233,201,164,0) 30%),
      radial-gradient(ellipse at 45% 80%, #d9674a 0%, rgba(217,103,74,0) 35%),
      linear-gradient(160deg, #ffffff 0%, #f4f1ee 40%, #e7ddd6 100%);
  }
  .services-band { position: absolute; inset: 0; }
  .brand {
    position: absolute; top: 88px; left: 0; width: 100%;
    display: flex; flex-direction: column; align-items: center;
  }
  .brand-name { color: var(--orange); font-size: 15px; font-weight: 400; letter-spacing: 0.5px; }
  .brand-tagline { color: var(--ink); font-size: 9px; margin-top: 2px; }
  .headline {
    position: absolute; top: 140px; left: 0; width: 100%;
    text-align: center; color: var(--orange);
    font-size: 46px; font-weight: 700; letter-spacing: -0.5px;
  }
  .intro {
    position: absolute; top: 205px; left: 70px; width: 470px;
    font-size: 11.5px; line-height: 1.35; color: var(--ink);
  }
  .services {
    position: absolute; left: 40px; top: 700px;
    width: 640px;
    transform: rotate(-19deg); transform-origin: left top;
  }
  .services-title {
    font-size: 30px; font-weight: 700; color: var(--ink);
    margin: 0 0 14px 170px;
  }
  .service-list { display: flex; gap: 8px; list-style: none; }
  .service { width: 90px; display: flex; flex-direction: column; align-items: center; }
  .service-icon {
    width: 62px; height: 62px; border-radius: 50%;
    border: 2px solid var(--white);
    display: flex; align-items: center; justify-content: center;
    color: var(--white); font-size: 11px; letter-spacing: 1px;
  }
  .service-text {
    margin-top: 8px; color: var(--white);
    font-size: 8.5px; line-height: 1.25; text-align: center;
  }
  .website {
    position: absolute; left: 350px; top: 880px;
    transform: rotate(-19deg); transform-origin: left top;
    color: var(--white); font-size: 13px; font-weight: 700;
    white-space: nowrap;
  }
</style>
</head>
<body>
  <article class="flyer">
    <div class="hero-photo" role="img" aria-label="Bright photo of a mother smiling at her baby by a sunlit window"></div>

    <svg class="services-band" viewBox="0 0 640 906" aria-hidden="true">
      <defs>
        <linearGradient id="bandFill" x1="1" y1="0" x2="0" y2="1">
          <stop offset="0" stop-color="#d9441f" stop-opacity="0.88"/>
          <stop offset="0.6" stop-color="#e8552b" stop-opacity="0.9"/>
          <stop offset="1" stop-color="#f08a2c" stop-opacity="0.92"/>
        </linearGradient>
      </defs>
      <polygon points="0,640 640,400 640,906 0,906" fill="url(#bandFill)"/>
      <polygon points="420,482 640,400 640,440 470,505" fill="#c23a1a" opacity="0.35"/>
    </svg>

    <header class="brand">
      <span class="brand-name">MERIDIAN ADVISORY</span>
      <span class="brand-tagline">Clear advice. Lasting results.</span>
    </header>

    <h1 class="headline">The Digital Revolution</h1>

    <p class="intro">For over 35 years Meridian CEO Daniel Hart has prospered on the “Cutting Edge” of Business and Finance. With extensive qualifications, comprehensive and wide ranging hands-on experience, he offers a unique and potent combination of expertise and knowledge that will guarantee superior strategic advice that can really make a difference.</p>

    <section class="services">
      <h2 class="services-title">Services</h2>
      <ul class="service-list">
        <li class="service"><span class="service-icon">ICON</span><p class="service-text">Business tax returns and planning for owners.</p></li>
        <li class="service"><span class="service-icon">ICON</span><p class="service-text">Super fund setup, audit and trustee compliance.</p></li>
        <li class="service"><span class="service-icon">ICON</span><p class="service-text">Bookkeeping, payroll and BAS lodgement on time.</p></li>
        <li class="service"><span class="service-icon">ICON</span><p class="service-text">Investment structuring and advice for growing families.</p></li>
        <li class="service"><span class="service-icon">ICON</span><p class="service-text">Retirement planning to protect your future income.</p></li>
        <li class="service"><span class="service-icon">ICON</span><p class="service-text">Cloud accounting setup and training for businesses.</p></li>
      </ul>
    </section>

    <p class="website">www.meridianadvisory.com.au</p>
  </article>
</body>
</html>
```